Photoshop our product at a wedding

We make a very customized hand sanitizer. We'd like to show it on display, ready for use, at a wedding venue. The project has three parts, of which you will do two. First, find or create a great picture of a bride or bride and groom that I can put on the hand sanitizer above the cake. Second, I will have that picture printed and put on the hand sanitizer, then will take the picture against a green screen. Third, I will send you that picture and you'll Photoshop it into the wedding venue picture.

After this is complete, I'll ask you to create your own picture for a wedding decoration. I'll take care of the 3D object design and production, and you design the photo for the tower and the venue. We'd like to continue this collaboration and produce many different options for wedding couples.

```html
<!DOCTYPE html>
<html lang="en">
<head>
<meta charset="utf-8">
<title>Customized Hand Sanitizer – Bottle Pair</title>
<link rel="stylesheet" href="https://fonts.googleapis.com/css2?family=Crimson+Text:wght@400&family=Sansita:wght@800&display=swap">
<style>
  :root {
    --page: #ffffff;
    --pump: #1fbf66;
    --pump-dark: #17a557;
    --pump-light: #4fd88a;
    --gel: #c8eedc;
    --gel-deep: #a6e2c6;
    --gel-edge: #8fd6b5;
    --neck: #e4f4ee;
    --label: #ffffff;
    --ink: #1a1a1a;
    --brand-green: #148a48;
    --wave-green: #1ea34f;
    --sky-top: #4f86d4;
    --sky-low: #b9d0ee;
    --dress: #dfe5ec;
    --suit: #243457;
  }
  * { margin: 0; padding: 0; box-sizing: border-box; }
  html, body {
    width: 1200px;
    height: 1200px;
    overflow: hidden;
    background: var(--page);
  }
  .canvas {
    position: relative;
    width: 1200px;
    height: 1200px;
  }
  .bottle {
    position: absolute;
    top: 138px;
    width: 340px;
    height: 900px;
  }
  .bottle--left { left: 164px; }
  .bottle--right { left: 697px; }
  .bottle-shape {
    position: absolute;
    inset: 0;
    width: 340px;
    height: 900px;
  }
  .label {
    position: absolute;
    left: 38px;
    top: 284px;
    width: 260px;
    height: 544px;
    background: var(--label);
    border-radius: 130px / 125px;
    overflow: hidden;
  }
  .label-eyebrow {
    position: absolute;
    top: 38px;
    left: 0;
    right: 0;
    text-align: center;
    font-family: "Crimson Text", serif;
    font-size: 19px;
    line-height: 26px;
    color: var(--ink);
  }
  .label-title {
    position: absolute;
    top: 80px;
    left: 0;
    right: 0;
    text-align: center;
    font-family: "Sansita", sans-serif;
    font-weight: 800;
    font-size: 41px;
    line-height: 48px;
    letter-spacing: 1px;
    color: var(--brand-green);
  }
  .label-wave {
    position: absolute;
    top: 198px;
    left: 0;
    width: 260px;
    height: 42px;
  }
  .label-photo {
    position: absolute;
    top: 234px;
    left: 0;
    width: 260px;
    height: 310px;
    background:
      linear-gradient(90deg, var(--dress) 0%, var(--dress) 46%, var(--suit) 60%, var(--suit) 100%) bottom / 100% 62% no-repeat,
      linear-gradient(180deg, var(--sky-top) 0%, var(--sky-low) 70%, #dbe6f4 100%);
  }
</style>
</head>
<body>
  <main class="canvas">
    <article class="bottle bottle--left">
      <svg class="bottle-shape" viewBox="0 0 340 900" aria-hidden="true">
        <path d="M110 176 L0 262 L0 860 Q0 888 28 888 L298 888 Q326 888 326 860 L326 262 L218 176 Z" fill="var(--gel)" stroke="var(--gel-edge)" stroke-width="2"/>
        <path d="M8 270 L8 856 L30 856 L30 270 Z M296 270 L296 856 L318 856 L318 270 Z" fill="var(--gel-deep)" opacity="0.6"/>
        <rect x="110" y="138" width="108" height="40" rx="4" fill="var(--neck)" stroke="#cfe6dc" stroke-width="2"/>
        <rect x="112" y="50" width="104" height="92" rx="6" fill="var(--pump)"/>
        <rect x="112" y="50" width="104" height="14" fill="var(--pump-light)"/>
        <rect x="150" y="6" width="46" height="46" fill="var(--pump-dark)"/>
        <path d="M46 10 L196 2 L196 22 L70 26 Q52 27 46 20 Z" fill="var(--pump)"/>
      </svg>
      <section class="label">
        <p class="label-eyebrow">CUSTOMIZED</p>
        <h1 class="label-title">Hand<br>Sanitizer</h1>
        <svg class="label-wave" viewBox="0 0 260 42" preserveAspectRatio="none" aria-hidden="true">
          <path d="M0 4 C70 18 130 18 260 12 L260 42 L0 42 Z" fill="var(--wave-green)"/>
          <path d="M0 34 C80 30 160 30 260 32 L260 42 L0 42 Z" fill="var(--label)"/>
        </svg>
        <div class="label-photo" role="img" aria-label="Photo of a bride in a white gown and a groom in a navy suit under a blue sky"></div>
      </section>
    </article>

    <article class="bottle bottle--right">
      <svg class="bottle-shape" viewBox="0 0 340 900" aria-hidden="true">
        <path d="M110 176 L0 262 L0 860 Q0 888 28 888 L298 888 Q326 888 326 860 L326 262 L218 176 Z" fill="var(--gel)" stroke="var(--gel-edge)" stroke-width="2"/>
        <path d="M8 270 L8 856 L30 856 L30 270 Z M296 270 L296 856 L318 856 L318 270 Z" fill="var(--gel-deep)" opacity="0.6"/>
        <rect x="110" y="138" width="108" height="40" rx="4" fill="var(--neck)" stroke="#cfe6dc" stroke-width="2"/>
        <rect x="112" y="50" width="104" height="92" rx="6" fill="var(--pump)"/>
        <rect x="112" y="50" width="104" height="14" fill="var(--pump-light)"/>
        <rect x="150" y="6" width="46" height="46" fill="var(--pump-dark)"/>
        <path d="M46 10 L196 2 L196 22 L70 26 Q52 27 46 20 Z" fill="var(--pump)"/>
      </svg>
      <section class="label">
        <p class="label-eyebrow">CUSTOMIZED</p>
        <h2 class="label-title">Hand<br>Sanitizer</h2>
        <svg class="label-wave" viewBox="0 0 260 42" preserveAspectRatio="none" aria-hidden="true">
          <path d="M0 4 C70 18 130 18 260 12 L260 42 L0 42 Z" fill="var(--wave-green)"/>
          <path d="M0 34 C80 30 160 30 260 32 L260 42 L0 42 Z" fill="var(--label)"/>
        </svg>
        <div class="label-photo" role="img" aria-label="Photo of a bride in a white gown and a groom in a navy suit under a blue sky"></div>
      </section>
    </article>
  </main>
</body>
</html>
```